KTW Structural Approval Partners Certifiers

Professional Construction Consultancy Company Business Card - must keep logo colours see images below - examples have been added from my last competition - please see them as examples only!

Target Market(s)

Home Builders

Industry/Entity Type

Construction

Contact Information for Business Card

See "must haves"

Font styles to use
Sans Serif

Colors
ffffff
add136
000000

Requirements
Must have
• Daniel Moravec
• Director
• Phone: 0431 758 219
• Address: 17 Corrigan St,
• Holloway Vale, SA, 5098
• Email: ktwapprovalpartners@mailbox-example.com
• Website: www.ktwapprovalpartners.example.au
• Facebook: KTW Structural Approval Partners
Nice to have
• Side 1: full logo
• Side 2: company details
Should not have
• hard to read
• must be clear and professional

```html
<!DOCTYPE html>
<html lang="en">
<head>
<meta charset="utf-8">
<title>KTW Structural Approval Partners – Business Card</title>
<link rel="stylesheet" href="https://fonts.googleapis.com/css2?family=Open+Sans:wght@400;600;700&display=swap">
<style>
  :root {
    --stage: #ece8e4;
    --card: #1f2a33;
    --lime: #add136;
    --white: #ffffff;
    --ink: #000000;
  }
  * { margin: 0; padding: 0; box-sizing: border-box; }
  html, body { width: 1200px; height: 900px; overflow: hidden; }
  body {
    background: var(--stage);
    font-family: "Open Sans", sans-serif;
    position: relative;
  }
  .card {
    position: absolute;
    background: var(--card);
    color: var(--white);
    box-shadow: 0 6px 18px rgba(0,0,0,0.25);
    overflow: hidden;
  }
  .card--details { left: 238px; top: 62px; width: 555px; height: 343px; }
  .card--brand { left: 457px; top: 518px; width: 560px; height: 344px; }

  .wordmark-small {
    position: absolute;
    left: 44px; top: 132px;
    display: flex; align-items: center; gap: 9px;
    color: var(--lime);
    font-weight: 700;
    font-size: 60px;
    line-height: 1;
    letter-spacing: 1px;
  }
  .wordmark-square { width: 13px; height: 13px; background: var(--lime); }

  .contact {
    position: absolute;
    left: 252px; top: 64px;
    font-size: 13px;
    line-height: 20px;
    white-space: nowrap;
  }
  .contact__name { color: var(--lime); font-weight: 600; font-size: 19px; line-height: 24px; }
  .contact__role { margin-bottom: 12px; }
  .contact__address { margin-bottom: 10px; }
  .contact__line { display: flex; align-items: center; gap: 8px; }
  .contact__line svg { width: 11px; height: 11px; flex: none; }

  .social {
    position: absolute;
    left: 0; right: 0; top: 289px;
    display: flex; align-items: center; gap: 10px;
    font-size: 14.5px;
    color: var(--lime);
    white-space: nowrap;
  }
  .social::before, .social::after {
    content: ""; height: 1px; background: var(--lime); opacity: 0.8;
  }
  .social::before { flex: 0 0 132px; }
  .social::after { flex: 1; }
  .social strong { font-weight: 700; }

  .brand-lockup {
    position: absolute;
    left: 0; right: 0; top: 118px;
    display: flex; align-items: center; justify-content: center; gap: 14px;
    color: var(--lime);
    font-weight: 700;
  }
  .brand-lockup__mark { font-size: 64px; line-height: 1; letter-spacing: 1px; }
  .brand-lockup__rule { width: 2px; height: 64px; background: var(--white); }
  .brand-lockup__words { font-size: 19px; line-height: 22px; text-transform: uppercase; }
  .brand-lockup__sub {
    position: absolute; left: 0; right: 0; top: 196px;
    text-align: center;
    color: var(--white);
    font-size: 16px; font-weight: 600; letter-spacing: 4px;
    text-transform: uppercase;
  }
</style>
</head>
<body>
  <section class="card card--details">
    <div class="wordmark-small"><span class="wordmark-square"></span>KTW</div>
    <div class="contact">
      <div class="contact__name">Daniel Moravec</div>
      <div class="contact__role">Director</div>
      <div class="contact__address">17 Corrigan St,<br>Holloway Vale, SA, 5098</div>
      <div class="contact__line">
        <svg viewBox="0 0 12 12"><path fill="#add136" d="M2.5 0.5l2 2-1 1.5c.6 1.5 1.9 2.9 3.5 3.5l1.5-1 2 2-1.3 2C5 10.5 1.5 7 0.5 1.8z"/></svg>
        0431 758 219
      </div>
      <div class="contact__line">
        <svg viewBox="0 0 12 12"><rect x="0.5" y="2.5" width="11" height="7" fill="#add136"/><path d="M0.5 2.5l5.5 4 5.5-4" fill="none" stroke="#1f2a33" stroke-width="1"/></svg>
        ktwapprovalpartners@mailbox-example.com
      </div>
      <div class="contact__line">
        <svg viewBox="0 0 12 12"><circle cx="6" cy="6" r="5.3" fill="none" stroke="#add136" stroke-width="1.3"/><path d="M0.7 6h10.6M6 0.7c-3 3-3 7.6 0 10.6M6 0.7c3 3 3 7.6 0 10.6" fill="none" stroke="#add136" stroke-width="1"/></svg>
        www.ktwapprovalpartners.example.au
      </div>
    </div>
    <div class="social"><span><strong>Facebook:</strong> KTW Structural Approval Partners</span></div>
  </section>

  <section class="card card--brand">
    <div class="brand-lockup">
      <span class="brand-lockup__mark">KTW</span>
      <span class="brand-lockup__rule"></span>
      <span class="brand-lockup__words">Structural<br>Approval<br>Partners</span>
    </div>
    <div class="brand-lockup__sub">Certifiers</div>
  </section>
</body>
</html>
```